Business card for Chiropractic clinics needs reworked / redesigned

The business card in attachment was designed 10 years ago. It is in need of an update.
We have 2 clinics:
VELDHOVE KLINIEK & VELDHOVE KLINIEK NOORD
Only one address needs to be on the card for doctors that only work in one clinic and two addresses need to be on the card for the doctors that work in both clinics.

Target Market(s)

patients/referrers

Industry/Entity Type

Medical

Contact Information for Business Card

Logo (in full or zoomed-in)
Clinic Name
Doctor name and title
clinic address, website, tel, email

Font styles to use
Sans Serif

Colors

Designer to choose colors to be used in the design.

Requirements
Must have
• Good contrast/readability
• We like modern minimalistic designs
• The Bcard needs to project our very high standard of proficiency/professionalism
Should not have
• Not curly
• Not to much colours

```html
<!DOCTYPE html>
<html lang="nl">
<head>
<meta charset="utf-8">
<title>Veldhove Kliniek – visitekaartje</title>
<link rel="stylesheet" href="https://fonts.googleapis.com/css2?family=Ubuntu:wght@400;700&display=swap">
<style>
  :root {
    --page: #ecebe8;
    --card-deep: #1f5773;
    --card-band: #2199b0;
    --accent: #17849c;
    --text-light: #ffffff;
  }
  html, body {
    margin: 0;
    padding: 0;
    width: 1200px;
    height: 1096px;
    overflow: hidden;
    background: var(--page);
    font-family: "Ubuntu", sans-serif;
  }
  .sheet {
    width: 1200px;
    height: 1096px;
    display: flex;
    flex-direction: column;
    align-items: center;
    justify-content: center;
    gap: 48px;
  }
  .card {
    width: 820px;
    height: 480px;
    position: relative;
    overflow: hidden;
    background: var(--card-deep);
    color: var(--text-light);
    box-shadow: 0 6px 18px rgba(0,0,0,0.18);
  }
  /* front */
  .spine-band {
    position: absolute;
    left: 0;
    top: 0;
    width: 820px;
    height: 480px;
  }
  .doctor {
    position: absolute;
    left: 70px;
    top: 52px;
    line-height: 1.2;
  }
  .doctor p { margin: 0; }
  .doctor-name { font-size: 30px; font-weight: 700; }
  .doctor-title, .doctor-number { font-size: 26px; font-weight: 400; letter-spacing: 0.5px; }
  .clinic-name {
    position: absolute;
    left: 70px;
    top: 190px;
    margin: 0;
    font-size: 46px;
    font-weight: 700;
    letter-spacing: 1px;
  }
  .address {
    position: absolute;
    left: 70px;
    top: 276px;
    display: flex;
    align-items: flex-start;
    gap: 16px;
    font-size: 26px;
    line-height: 1.2;
  }
  .address svg { flex: none; margin-top: 2px; }
  .contact {
    position: absolute;
    left: 420px;
    top: 276px;
    font-size: 24px;
    line-height: 1.3;
  }
  .contact p { margin: 0; }
  /* back */
  .band {
    height: 118px;
    background: var(--card-band);
    display: flex;
    align-items: center;
    justify-content: center;
  }
  .band-name {
    margin: 0;
    font-size: 44px;
    font-weight: 700;
    letter-spacing: 1.5px;
    color: var(--card-deep);
  }
  .mark-area {
    position: absolute;
    left: 150px;
    top: 170px;
    width: 520px;
    height: 250px;
    border-radius: 12px;
    background: linear-gradient(180deg, rgba(33,153,176,0.38), rgba(33,153,176,0.16));
  }
</style>
</head>
<body>
<main class="sheet">
  <section class="card card-front" aria-label="Voorzijde visitekaartje">
    <svg class="spine-band" viewBox="0 0 820 480" aria-hidden="true">
      <path d="M -30 392 C 180 470, 480 415, 860 470" fill="none" stroke="var(--accent)" stroke-width="46"/>
    </svg>
    <div class="doctor">
      <p class="doctor-name">Pieter VANDAMME D.C</p>
      <p class="doctor-title">CHIROPRACTOR</p>
      <p class="doctor-number">09.12345.67.000</p>
    </div>
    <h1 class="clinic-name">VELDHOVE KLINIEK</h1>
    <div class="address">
      <svg width="30" height="40" viewBox="0 0 30 40" aria-hidden="true">
        <path d="M15 1C7 1 1 7 1 15c0 10 14 24 14 24s14-14 14-24C29 7 23 1 15 1z" fill="var(--accent)"/>
        <circle cx="15" cy="15" r="5" fill="var(--card-deep)"/>
      </svg>
      <div>Kouterlaan 48<br>9000 Gent</div>
    </div>
    <div class="contact">
      <p>T: +32 (0)9 555.01.23</p>
      <p>info@veldhovekliniek.be</p>
      <p>www.veldhovekliniek.be</p>
    </div>
  </section>

  <section class="card card-back" aria-label="Achterzijde visitekaartje">
    <div class="band">
      <h2 class="band-name">VELDHOVE KLINIEK</h2>
    </div>
    <div class="mark-area" role="img" aria-label="Plaats voor het beeldmerk van de kliniek"></div>
  </section>
</main>
</body>
</html>
```